Delia Forsby Space Tamer

a larger business card may standard size 4” x 9” describing what I do. I don’t know if this would be considered a flyer. I rearrange, redesign and stage houses for the owner or to sell.

```html
<!DOCTYPE html>
<html lang="en">
<head>
<meta charset="utf-8">
<title>Delia Forsby — Space Tamer</title>
<link href="https://fonts.googleapis.com/css2?family=Lora:ital,wght@0,400;0,600;0,700;1,400;1,600&family=Lato:wght@400;700&display=swap" rel="stylesheet">
<style>
  :root{
    --backdrop:#5f5f5f;
    --paper:#ffffff;
    --brick:#8b2a1f;
    --teal:#00b5b5;
    --ink:#1f1f1f;
    --accent-red:#a8261b;
  }
  html,body{margin:0;padding:0;width:1200px;height:1200px;overflow:hidden;background:var(--backdrop);}
  .card{position:absolute;top:160px;width:390px;height:880px;background:var(--paper);box-shadow:2px 3px 6px rgba(0,0,0,.35);overflow:hidden;}
  .card--front{left:185px;}
  .card--back{left:622px;}

  /* front */
  .front-header{position:absolute;left:0;top:0;width:100%;height:117px;text-align:center;}
  .front-name{margin:0;padding-top:42px;font-family:"Lora",serif;font-weight:700;font-size:33px;letter-spacing:3px;color:var(--ink);line-height:1;}
  .front-title{margin:4px 0 0;font-family:"Lora",serif;font-style:italic;font-size:16px;letter-spacing:1px;color:var(--ink);}
  .front-rule{position:absolute;left:0;width:100%;background:var(--brick);}
  .front-rule--top{top:117px;height:4px;}
  .front-rule--bottom{top:794px;height:3px;}
  .front-photo{position:absolute;left:0;top:121px;width:100%;height:637px;
    background:linear-gradient(180deg,#b3452f 0%,#a94631 30%,#c9b5a8 45%,#d9b9a4 60%,#2aa79d 80%,#1f9f98 100%);}
  .front-tagline{position:absolute;left:0;top:758px;width:100%;height:36px;display:flex;align-items:center;justify-content:center;
    font-family:"Lora",serif;font-style:italic;font-weight:600;font-size:15px;color:var(--ink);}
  .front-footer{position:absolute;left:0;top:797px;width:100%;height:83px;background:var(--brick);display:flex;align-items:center;justify-content:center;
    text-align:center;font-family:"Lora",serif;font-weight:600;font-size:16px;line-height:22px;letter-spacing:.8px;color:var(--paper);}

  /* back */
  .contact-strip{position:absolute;left:24px;top:25px;width:31px;height:829px;background:var(--brick);}
  .about-panel{position:absolute;left:55px;top:25px;width:312px;height:829px;background:var(--teal);}
  .rotated{position:absolute;left:50%;top:50%;transform:translate(-50%,-50%) rotate(90deg);}
  .contact-line{width:829px;height:31px;display:flex;align-items:center;box-sizing:border-box;padding-left:24px;
    font-family:"Lora",serif;font-size:14px;letter-spacing:.5px;color:var(--paper);}
  .contact-item{display:flex;align-items:center;gap:7px;white-space:nowrap;}
  .contact-item svg{width:13px;height:13px;fill:var(--paper);}
  .contact-phone{width:190px;}
  .contact-email{width:280px;}
  .about-text{width:829px;height:312px;text-align:center;font-family:"Lato",sans-serif;color:var(--paper);box-sizing:border-box;padding:20px 24px 0;}
  .about-headline{margin:0 0 14px;font-weight:700;font-size:21px;line-height:25px;}
  .about-body{margin:0;font-size:12px;line-height:20.5px;}
  .about-body .highlight{color:var(--accent-red);font-weight:700;}
  .about-gap{display:block;height:19px;}
</style>
</head>
<body>
  <section class="card card--front">
    <header class="front-header">
      <h1 class="front-name">DELIA FORSBY</h1>
      <p class="front-title">(a Space Tamer)</p>
    </header>
    <div class="front-rule front-rule--top"></div>
    <div class="front-photo" role="img" aria-label="Portrait photo of Delia Forsby in a teal top, in a room with a red wall"></div>
    <div class="front-tagline">Homes: Rearranged. Redesigned. Staged to Sell.</div>
    <div class="front-rule front-rule--bottom"></div>
    <div class="front-footer">With little or no cost, Delia breathes<br>new life &amp; energy into your home.</div>
  </section>

  <section class="card card--back">
    <div class="contact-strip">
      <div class="rotated contact-line">
        <span class="contact-item contact-phone">
          <svg viewBox="0 0 24 24"><path d="M6.6 10.8a15 15 0 0 0 6.6 6.6l2.2-2.2a1 1 0 0 1 1-.25 11.4 11.4 0 0 0 3.6.57 1 1 0 0 1 1 1V20a1 1 0 0 1-1 1A17 17 0 0 1 3 4a1 1 0 0 1 1-1h3.5a1 1 0 0 1 1 1c0 1.25.2 2.45.57 3.6a1 1 0 0 1-.25 1z"/></svg>
          503-555-0148
        </span>
        <span class="contact-item contact-email">
          <svg viewBox="0 0 24 24"><path d="M3 5h18v14H3z M3 5l9 8 9-8" fill="none" stroke="#fff" stroke-width="2.5"/></svg>
          deliaforsby@examplemail.net
        </span>
        <span class="contact-item contact-address">
          <svg viewBox="0 0 24 24"><path d="M12 2a7 7 0 0 0-7 7c0 5 7 13 7 13s7-8 7-13a7 7 0 0 0-7-7zm0 9.5A2.5 2.5 0 1 1 12 6.5a2.5 2.5 0 0 1 0 5z"/></svg>
          4210 S. Larkin Drive, Yuma, AZ 85365
        </span>
      </div>
    </div>
    <div class="about-panel">
      <div class="rotated about-text">
        <h2 class="about-headline">For 36 years, Delia was a realestate Broker in Oregon. She has a track record<br>of transforming houses that do not sell into homes that sell quickly.</h2>
        <p class="about-body">
          <span class="highlight">As a Hearth &amp; Haven national award winner, her talent has not gone unnoticed.</span><br>
          She eagerly finds renewed energy by rearranging what you already have, and rethinking your space.<br>
          With a dash of this, a zest of that,<br>
          she virtually re-invigorates your environment.<br>
          Thrilled customers say...
          <span class="about-gap"></span>
          <span class="highlight">"This is just how I dreamed my home would look!"</span><br>
          Make your space livable, lovable and profitable...<br>
          ...a place where you or your buyer can hardly wait to come home to.<br>
          Voila!
        </p>
      </div>
    </div>
  </section>
</body>
</html>
```